High quality childcare centre needs a roadside banner

We need a banner designed that advertises our achievement of being rated Exceeding National Quality Standard. Which is the highest rating you can be award as part of the assessment and rating process.

Attached pdf is purely an example although the text as it stands needs to be incorporated.

Please see below for the corporate colors:

Magenta
C-0 M-100 Y-33 K-10
bf00bf

Green
C-78 M-0 Y-100 K-0
00bf00

Target Market(s)

Parents of young children that need childcare

Industry/Entity Type

Childcare

Font styles to use
Sans Serif

Requirements
Must have
• As it is a roadside banner the text should be big, bold and easy to read therefore do not use serif fonts
• Please change found to find
• Logo - see attached
• Supplied wording - see attached
• The specs for the banner are 4m x 1.25m or 4000mm x 1250mm
• The files need to be in the following format:
• jpg, eps and ai.
• Bleeds if relevant
Nice to have
• Other marketing road signs incorporate the attached 'grobold' font
• We also have a motto - 'out of little things, big things grow'
Should not have
• Serif fonts

```html
<!DOCTYPE html>
<html lang="en">
<head>
<meta charset="utf-8">
<title>Small Sprouts – Roadside Banner</title>
<link href="https://fonts.googleapis.com/css2?family=Chewy&family=Cormorant+Garamond:wght@500&display=swap" rel="stylesheet">
<style>
  :root {
    --backdrop: #c0c0c0;
    --magenta: #bb00bb;
    --magenta-shadow: #6e006e;
    --green: #00bf00;
    --white: #ffffff;
    --lavender: #a066d0;
    --teal: #1aa0b0;
    --gold: #f0b429;
    --olive: #9ab83a;
    --block-green: #c8e8a0;
    --book-mix: #5a8fb8;
    --ribbon: #b03050;
  }
  html, body {
    margin: 0;
    width: 1200px;
    height: 600px;
    overflow: hidden;
    background: var(--backdrop);
  }
  p, h1 { margin: 0; }
  .banner {
    position: absolute;
    left: 100px;
    top: 90px;
    width: 1000px;
    height: 418px;
    background: var(--magenta);
    overflow: hidden;
    font-family: "Chewy", "Arial Rounded MT Bold", sans-serif;
    color: var(--white);
  }
  .headline-group {
    position: absolute;
    z-index: 2;
    left: 58px;
    top: 88px;
    transform: rotate(-4deg);
    transform-origin: left top;
    text-shadow: 3px 3px 0 var(--magenta-shadow);
    text-transform: uppercase;
    white-space: nowrap;
  }
  .rating-intro {
    font-size: 26px;
    line-height: 1.1;
    margin: 0 0 6px 4px;
    letter-spacing: 1px;
  }
  .rating-title {
    font-size: 54px;
    line-height: 1.05;
    font-weight: 700;
    letter-spacing: 1px;
  }
  .call-to-action {
    position: absolute;
    z-index: 2;
    left: 240px;
    top: 262px;
    font-size: 22px;
    text-transform: uppercase;
    letter-spacing: 1px;
    white-space: nowrap;
    transform: rotate(-4deg);
    transform-origin: left top;
    text-shadow: 2px 2px 0 var(--magenta-shadow);
  }
  .motto {
    position: absolute;
    z-index: 2;
    left: 190px;
    top: 362px;
    font-family: "Cormorant Garamond", Georgia, serif;
    font-size: 24px;
    font-weight: 500;
    white-space: nowrap;
  }
  .deco {
    position: absolute;
    border-radius: 10px;
  }
  .deco--puzzle { left: 34px; top: 32px; width: 42px; height: 42px; background: var(--teal); transform: rotate(20deg); }
  .deco--cloud-small { left: 105px; top: 42px; width: 76px; height: 22px; background: var(--lavender); border-radius: 14px; }
  .deco--globe { left: 372px; top: 34px; width: 54px; height: 54px; background: var(--gold); border-radius: 50%; }
  .deco--cloud-large { left: 455px; top: 30px; width: 140px; height: 42px; background: var(--lavender); border-radius: 24px; }
  .deco--medal { left: 700px; top: 22px; width: 74px; height: 96px; background: linear-gradient(var(--ribbon) 0 45%, var(--gold) 45%); border-radius: 12px 12px 40px 40px; }
  .deco--books { left: 35px; top: 280px; width: 100px; height: 92px; background: linear-gradient(135deg, var(--gold), var(--book-mix)); }
  .deco--pencil { left: 172px; top: 262px; width: 52px; height: 50px; background: var(--green); transform: rotate(-35deg); border-radius: 16px; }
  .deco--cap { left: 390px; top: 302px; width: 60px; height: 50px; background: var(--olive); }
  .deco--blocks { left: 558px; top: 288px; width: 76px; height: 78px; background: var(--block-green); }
  .brand-disc {
    position: absolute;
    z-index: 1;
    left: 703px;
    top: 128px;
    width: 430px;
    height: 430px;
    border-radius: 50%;
    background: var(--white);
    box-shadow: 0 0 0 13px var(--green);
  }
  .brand-mark {
    position: absolute;
    z-index: 1;
    left: 828px;
    top: 202px;
    width: 64px;
    height: 64px;
    border-radius: 50%;
    background: var(--magenta);
  }
  .brand-name {
    position: absolute;
    z-index: 1;
    left: 725px;
    top: 290px;
    width: 270px;
    text-align: center;
    font-size: 36px;
    color: var(--green);
    white-space: nowrap;
  }
</style>
</head>
<body>
  <main class="banner">
    <div class="deco deco--puzzle" role="img" aria-label="Teal puzzle piece illustration"></div>
    <div class="deco deco--cloud-small" role="img" aria-label="Small lavender cloud illustration"></div>
    <div class="deco deco--globe" role="img" aria-label="Gold globe illustration"></div>
    <div class="deco deco--cloud-large" role="img" aria-label="Large lavender cloud illustration"></div>
    <div class="deco deco--medal" role="img" aria-label="Gold medal on ribbon illustration"></div>
    <div class="deco deco--books" role="img" aria-label="Stack of colourful books illustration"></div>
    <div class="deco deco--pencil" role="img" aria-label="Green pencil illustration"></div>
    <div class="deco deco--cap" role="img" aria-label="Graduation cap illustration"></div>
    <div class="deco deco--blocks" role="img" aria-label="ABC toy blocks illustration"></div>

    <div class="brand-disc"></div>
    <div class="brand-mark"></div>
    <p class="brand-name">Small Sprouts</p>

    <div class="headline-group">
      <p class="rating-intro">This service is rated</p>
      <h1 class="rating-title">‘Exceeding National<br>Quality Standard ’</h1>
    </div>
    <p class="call-to-action">Come in and find out why......</p>
    <p class="motto">out of little things, big things grow</p>
  </main>
</body>
</html>
```